Redesign of business card for Birchline Mechanical

We are looking for a new design for our business cards for Birchline Mechanical. We are a plumbing & HVAC construction company, operating on the West Coast of Canada and USA. Logo attached.
Industry/Entity Type
Construction - Plumbing & HVAC
Contact Information for Business Card
Name, address, phone numbers, email, website address
Look and feel
Each slider illustrates characteristics of the customer's brand and the style your logo design should communicate.

```html
<!DOCTYPE html>
<html lang="en">
<head>
<meta charset="UTF-8">
<title>Birchline Mechanical — Business Card</title>
<link rel="stylesheet" href="https://fonts.googleapis.com/css2?family=Lato:wght@400;700;900&display=swap">
<style>
  :root {
    --backdrop: #1b1b1c;
    --card: #232325;
    --card-edge: #2c2c2f;
    --accent-bar: #e4e4e6;
    --ink-strong: #ffffff;
    --ink-soft: #b9b9bd;
    --ink-muted: #8d8d92;
    --divider: #4a4a4f;
    --mark-silver: #c9c9cd;
  }
  * { box-sizing: border-box; margin: 0; padding: 0; }
  html, body {
    width: 1200px; height: 952px; overflow: hidden;
    background: var(--backdrop);
    font-family: "Lato", Arial, sans-serif;
  }
  .sheet {
    width: 1200px; height: 952px;
    display: flex; flex-direction: column;
    align-items: center; justify-content: center; gap: 48px;
  }
  .card {
    position: relative;
    width: 620px; height: 354px;
    background: var(--card);
    border: 1px solid var(--card-edge);
    overflow: hidden;
  }

  /* Contact side */
  .accent-bar { position: absolute; background: var(--accent-bar); width: 26px; }
  .accent-bar--top { left: 0; top: 0; height: 120px; }
  .accent-bar--bottom { right: 0; bottom: 0; height: 120px; }

  .brand {
    position: absolute; left: 62px; top: 118px; width: 230px;
    display: flex; align-items: center; gap: 12px;
  }
  .brand__square {
    width: 22px; height: 22px; background: var(--ink-strong); flex: none;
  }
  .brand__name {
    color: var(--ink-strong); font-weight: 700; font-size: 21px;
    letter-spacing: 1px; text-transform: uppercase; line-height: 1.2;
  }

  .divider {
    position: absolute; left: 318px; top: 52px;
    width: 1px; height: 196px; background: var(--divider);
  }

  .contact { position: absolute; left: 346px; top: 82px; }
  .contact__name {
    color: var(--ink-strong); font-size: 19px; letter-spacing: 1px;
    text-transform: uppercase; font-weight: 400;
  }
  .contact__name strong { font-weight: 900; }
  .contact__role { color: var(--ink-soft); font-size: 14px; margin-top: 2px; }
  .contact__list { list-style: none; margin-top: 16px; }
  .contact__item {
    display: flex; align-items: center; gap: 9px;
    color: var(--ink-soft); font-size: 13.5px; line-height: 24px;
  }
  .contact__item svg { width: 12px; height: 12px; fill: var(--ink-strong); flex: none; }

  .address {
    position: absolute; left: 0; right: 0; bottom: 38px;
    text-align: center; color: var(--ink-muted); font-size: 13px;
  }

  /* Logo side */
  .card--logo { display: flex; align-items: center; justify-content: center; gap: 16px; }
  .card--logo .brand__square { width: 34px; height: 34px; background: var(--mark-silver); }
  .card--logo .brand__name { color: var(--mark-silver); font-size: 32px; letter-spacing: 2px; }
</style>
</head>
<body>
<main class="sheet">
  <section class="card card--contact" aria-label="Business card, contact side">
    <div class="accent-bar accent-bar--top"></div>
    <div class="accent-bar accent-bar--bottom"></div>

    <div class="brand">
      <span class="brand__square"></span>
      <span class="brand__name">Birchline Mechanical</span>
    </div>

    <div class="divider"></div>

    <div class="contact">
      <h1 class="contact__name">Daniel R. <strong>Whitmore</strong></h1>
      <p class="contact__role">Managing Director</p>
      <ul class="contact__list">
        <li class="contact__item">
          <svg viewBox="0 0 24 24" aria-hidden="true"><path d="M6.6 10.8a15.1 15.1 0 0 0 6.6 6.6l2.2-2.2c.3-.3.7-.4 1-.2 1.1.4 2.3.6 3.6.6.6 0 1 .4 1 1V20c0 .6-.4 1-1 1A17 17 0 0 1 3 4c0-.6.4-1 1-1h3.5c.6 0 1 .4 1 1 0 1.3.2 2.5.6 3.6.1.3 0 .7-.2 1z"/></svg>
          +1 604 555 0182
        </li>
        <li class="contact__item">
          <svg viewBox="0 0 24 24" aria-hidden="true"><path d="M2 5h20v14H2z M2 5l10 8 10-8" /></svg>
          hello@birchlinemech.com
        </li>
        <li class="contact__item">
          <svg viewBox="0 0 24 24" aria-hidden="true"><circle cx="12" cy="12" r="10"/></svg>
          www.birchlinemech.com
        </li>
      </ul>
    </div>

    <p class="address">2217 Harbourview Drive Vancouver, BC V6B 1A4</p>
  </section>

  <section class="card card--logo" aria-label="Business card, logo side">
    <span class="brand__square"></span>
    <span class="brand__name">Birchline Mechanical</span>
  </section>
</main>
</body>
</html>
```